Curriculum design template for a mental health project

We have a curriculum for a 12-week mental health program, delivered in Uganda. Currently, the Word format is very basic. I would like a new template created on Word which we can edit in vertical A4 page format.

This Word template would include:
• A curriculum cover page incorporating a photo
• A page for acknowledgments
• A contents page
• Stage cover pages with space for images (there are 3 stages)
• Session cover pages with space for images (there are 12 sessions)
• Pages for activity descriptions; with a title and some introduction text, a section for materials needed and duration of activity (perhaps with icons of materials/clock, formatting to have a table with step-by-step instructions and a box where top tips/extra info can be added
• An optional page with extra information for an activity to be added
• A closing page

The organisation's website for colour palette/font and the logo is attached below: https://bloomkaseno.org/

Target Market(s)

Young peer leaders of the program will use this curriculum

Industry/Entity Type

NGO

Font styles to use
Serif

Colors
00AB8E
00BBA5
67D7C9
C6EFE9
E9F9F6
F0912C
F2A743
F7CA91
FBE8D2
FDF5EE

Requirements
Must have
• Editable Word document, structured activity pages with and places to add images
Nice to have
• Icons with activity description and time duration sections of the activity pages, nice stage cover pages with space for an image, description of the stage

```html
<!DOCTYPE html>
<html lang="en">
<head>
<meta charset="utf-8">
<title>Mental Health Curriculum – Cover</title>
<link rel="stylesheet" href="https://fonts.googleapis.com/css2?family=Archivo:wght@400;800&family=Inter:wght@400&display=swap">
<style>
  :root {
    --bg: #e2e2e2;
    --paper: #f1f1f1;
    --teal-dark: #00ab8e;
    --teal: #00bba5;
    --teal-light: #67d7c9;
    --mist: #d3dae6;
    --ink: #2b2b2b;
    --photo-sky: #e8ecee;
    --photo-leaf: #a9c98a;
    --photo-shirt: #3d4f8a;
  }
  html, body {
    margin: 0;
    width: 1200px;
    height: 840px;
    overflow: hidden;
    background: var(--bg);
  }
  .cover {
    position: absolute;
    left: 317px;
    top: 20px;
    width: 566px;
    height: 800px;
    background: var(--paper);
    overflow: hidden;
    box-shadow: 0 6px 24px rgba(0,0,0,.18);
  }
  .cover__photo {
    position: absolute;
    inset: 0;
    width: 100%;
    height: 100%;
  }
  .cover__tint {
    position: absolute;
    left: 0;
    top: 0;
    width: 270px;
    height: 178px;
    background: var(--teal);
    opacity: .55;
  }
  .brand {
    position: absolute;
    right: 34px;
    top: 66px;
    margin: 0;
    font-family: "Archivo", sans-serif;
    font-weight: 800;
    font-size: 18px;
    color: var(--teal-dark);
  }
  .side-tab {
    position: absolute;
    left: 0;
    top: 340px;
    width: 18px;
    height: 48px;
    background: var(--teal);
  }
  .title-shadow {
    position: absolute;
    left: 126px;
    top: 528px;
    width: 352px;
    height: 130px;
    background: var(--mist);
  }
  .title-block {
    position: absolute;
    left: 102px;
    top: 386px;
    width: 464px;
    height: 240px;
    background: linear-gradient(160deg, var(--teal-dark) 0%, var(--teal) 45%, var(--teal-light) 100%);
    color: #fff;
    box-sizing: border-box;
    padding: 42px 30px 0 66px;
  }
  .title-block__heading {
    margin: 0;
    font-family: "Archivo", sans-serif;
    font-weight: 800;
    font-size: 46px;
    line-height: 1.02;
  }
  .title-block__sub {
    position: relative;
    margin: 14px 0 0;
    font-family: "Inter", sans-serif;
    font-size: 17px;
    letter-spacing: .04em;
  }
  .title-block__rule {
    position: absolute;
    left: -102px;
    top: 10px;
    width: 92px;
    height: 1px;
    background: #fff;
  }
  .intro {
    position: absolute;
    left: 28px;
    top: 672px;
    width: 400px;
    margin: 0;
    font-family: "Inter", sans-serif;
    font-size: 10.5px;
    line-height: 1.55;
    color: var(--ink);
  }
  .foot-rule {
    position: absolute;
    left: 330px;
    right: 0;
    top: 752px;
    height: 1px;
    background: var(--teal);
  }
</style>
</head>
<body>
  <main class="cover">
    <svg class="cover__photo" viewBox="0 0 566 800" role="img" aria-label="Photo of five smiling young peer leaders sitting together outdoors under a tree">
      <defs>
        <linearGradient id="photoTone" x1="0" y1="0" x2="1" y2="1">
          <stop offset="0" stop-color="var(--photo-leaf)"/>
          <stop offset=".45" stop-color="var(--photo-sky)"/>
          <stop offset="1" stop-color="var(--photo-shirt)"/>
        </linearGradient>
      </defs>
      <path d="M0 0 H566 V520 H120 V320 H0 Z" fill="url(#photoTone)"/>
    </svg>
    <div class="cover__tint"></div>

    <p class="brand">Bloom Kaseno</p>

    <div class="side-tab"></div>
    <div class="title-shadow"></div>

    <section class="title-block">
      <h1 class="title-block__heading">Mental Health<br>Curriculum</h1>
      <p class="title-block__sub"><span class="title-block__rule"></span>Looking Back to Move Forward</p>
    </section>

    <p class="intro">Lorem ipsum dolor sit amet, consectetur adipiscing elit. Aenean tellus quam, tincidunt vitae suscipit sed, euismod at est. Donec et ligula ex.</p>
    <div class="foot-rule"></div>
  </main>
</body>
</html>
```